New Flyer Design Project

We need a flyer for our upcoming Rising Builders Forum.

5th Annual Rising Builders Forum
by the Council for Stewardship of Built Ventures (C-SBuV)
Theme: Step Forward
Date: January 24, 2020
Location: Bluestone Lodge Hotel and Conference Center, San Marcos, TX
#StepForward

This is event is put together by C-SBuV's Rising Builders Ring of Merit. I have a logo for the Ring of Merit, but not something that indicates it's the Rising Builders Ring.

More about the Forum (please don't include on the flyer): This Forum provides a venue to openly discuss issues affecting women in our industry and ideas and strategies to address those issues.

Architecture, Construction and Engineering are all struggling with a tremendous shortage of skilled talent. It is more important than ever for organizations to be able to attract, support and retain a talented workforce and to encourage more women to pursue and build vibrant careers in architecture, engineering and construction. Unfortunately, their attrition rate also remains high in these industries. Developing and retaining a skilled workforce includes identifying and addressing the specific needs of women in our industry. Man or Woman; Male or Female Brain, C-SBuV’s Rising Builders Forum will give you and your team the tools you need to excel as an Employer of Choice and a roadmap for individual continued career planning and success .

This unique Forum provides a venue to engage everyone from executives to those just beginning their careers with active, hands-on sessions and vibrant networking with the best and brightest in the A/E/C industry. In our usual C-SBuV Forum style, Keynotes become table participants and table participants become presenters, encouraging participants to assimilate what they are learning. Join local, state and national leaders and subject matter experts as we candidly explore and address the issues affecting women in our industry .

```html
<!DOCTYPE html>
<html lang="en">
<head>
<meta charset="utf-8">
<title>5th Annual Rising Builders Forum</title>
<link href="https://fonts.googleapis.com/css2?family=Montserrat:wght@700;800&family=Libre+Baskerville&family=Bebas+Neue&family=Oswald:wght@500&display=swap" rel="stylesheet">
<style>
  :root {
    --magenta: #e0309e;
    --pink: #f132a3;
    --purple: #8a6fcb;
    --blue: #22b4ec;
    --lime: #d4df2d;
    --coral: #f25a5a;
    --white: #f4f4f4;
    --ink: #1b1b1b;
    --blue-shadow: #1aa8e8;
  }
  html, body { margin: 0; padding: 0; overflow: hidden; }
  .flyer {
    position: relative;
    width: 848px; height: 1200px;
    overflow: hidden;
    background: var(--magenta);
    font-family: "Montserrat", sans-serif;
    color: var(--white);
  }
  .backdrop {
    position: absolute; inset: 0;
    background:
      linear-gradient(180deg, rgba(241,50,163,0) 55%, var(--pink) 85%),
      linear-gradient(120deg, #d826a0 0%, #b73aa9 30%, var(--purple) 55%, var(--blue) 85%);
  }
  .edition { position: absolute; left: 32px; top: 88px; font-weight: 800; line-height: 1; }
  .edition-number { font-size: 72px; letter-spacing: -1px; }
  .edition-word { font-size: 33px; margin-top: -6px; }
  .marker { position: absolute; }
  .host-band {
    position: absolute; left: 402px; top: 114px; width: 446px; height: 19px;
    background: var(--lime); color: var(--ink);
    font-family: "Libre Baskerville", serif; font-size: 12.5px;
    line-height: 19px; padding-left: 26px; box-sizing: border-box; white-space: nowrap;
  }
  .ring-badge {
    position: absolute; left: 281px; top: 243px; width: 148px; height: 82px;
    background: #fff; box-shadow: 6px 6px 0 var(--blue-shadow);
    display: flex; align-items: center; justify-content: center; gap: 8px;
    font-family: "Montserrat", sans-serif; font-weight: 700; font-size: 15px; color: #4d5a9a;
  }
  .ring-badge .dot { width: 18px; height: 18px; border-radius: 50%; background: #4d5a9a; }
  .headline {
    position: absolute; left: 280px; top: 342px; margin: 0;
    font-weight: 800; font-size: 96px; line-height: 92px; letter-spacing: 0;
    text-transform: uppercase; white-space: nowrap;
  }
  .hashtag-band {
    position: absolute; left: 0; top: 694px; width: 272px; height: 69px;
    background: var(--lime); color: var(--coral);
    font-family: "Bebas Neue", sans-serif; font-size: 42px; line-height: 69px;
    padding-left: 34px; box-sizing: border-box; letter-spacing: 1px;
  }
  .schedule {
    position: absolute; right: 88px; top: 736px; text-align: right;
    font-weight: 700; font-size: 35px; line-height: 46px;
  }
  .rule { position: absolute; left: 547px; top: 848px; width: 208px; height: 14px; background: var(--lime); }
  .venue {
    position: absolute; left: 0; width: 870px; top: 1063px; text-align: center;
    font-family: "Oswald", sans-serif; font-weight: 500; font-size: 17px; line-height: 22px;
    text-transform: uppercase;
  }
  .more-info {
    position: absolute; left: 0; width: 870px; top: 1142px; text-align: center;
    font-family: "Libre Baskerville", serif; font-size: 14px; color: var(--lime); text-transform: uppercase;
  }
  .more-info .site { color: var(--white); }
</style>
</head>
<body>
<main class="flyer">
  <div class="backdrop" role="img" aria-label="Faceted geometric background in magenta, violet and sky blue"></div>

  <div class="edition">
    <div class="edition-number">5TH</div>
    <div class="edition-word">ANNUAL</div>
  </div>
  <svg class="marker" style="left:89px;top:212px" width="35" height="29" aria-hidden="true"><polygon points="0,0 35,0 17.5,29" fill="#d4df2d"/></svg>

  <div class="host-band">The Council for Stewardship of Built Ventures (C-SBuV)</div>

  <div class="ring-badge"><span class="dot"></span>Ring of Merit</div>

  <h1 class="headline">Rising<br>Builders<br>Forum</h1>

  <div class="hashtag-band">#StepForward</div>

  <svg class="marker" style="left:634px;top:680px" width="35" height="29" aria-hidden="true"><polygon points="0,0 35,0 17.5,29" fill="#d4df2d"/></svg>

  <div class="schedule">JAN 24, 2020<br>10AM - 4PM</div>
  <div class="rule"></div>

  <svg class="marker" style="left:400px;top:969px" width="70" height="61" aria-hidden="true"><polygon points="35,0 70,61 0,61" fill="#d4df2d"/></svg>

  <div class="venue">Bluestone Lodge Hotel and Conference Center<br>1450 Ridgeline Ave, San Marcos, TX</div>

  <div class="more-info">Visit <span class="site">c-sbuv.eventhub.org</span> for more information</div>
</main>
</body>
</html>
```